Residential Roofing Company, need a Unique business card for a Woman owned ompany

Woman Owned Residential Roofing Company. Specializing in Insurance Claims
Attention to Detail is what sets this woman owned roofing company apart from the rest
We are TRV Certified and are an Accredited business with an A rating with the QPL. Our Contractor License number KMT48395

```html
<!DOCTYPE html>
<html lang="en">
<head>
<meta charset="utf-8">
<title>Crestline Roofing — Business Card</title>
<link href="https://fonts.googleapis.com/css2?family=Open+Sans:wght@400;600;800&display=swap" rel="stylesheet">
<style>
  :root {
    --navy: #24335f;
    --navy-deep: #1d2a50;
    --badge-blue: #1f5a8c;
    --white: #ffffff;
    --ink: #2b2b2b;
    --backdrop: #e9eaec;
  }
  * { margin: 0; padding: 0; box-sizing: border-box; }
  html, body { width: 1200px; height: 801px; overflow: hidden; }
  body {
    background: var(--backdrop);
    font-family: "Open Sans", Arial, sans-serif;
    position: relative;
  }
  .card {
    position: absolute;
    width: 540px;
    height: 310px;
    border-radius: 22px;
    box-shadow: 0 6px 18px rgba(0,0,0,0.18);
  }
  /* Back side */
  .card-back {
    left: 40px; top: 110px;
    background: var(--navy);
    color: var(--white);
    display: flex; flex-direction: column;
    align-items: center; justify-content: center;
  }
  .wordmark {
    display: flex; align-items: center; gap: 12px;
    font-weight: 800; font-size: 36px; letter-spacing: 0.5px;
    text-transform: uppercase;
  }
  .wordmark-square { width: 22px; height: 22px; background: currentColor; }
  .card-back .license {
    margin-top: 56px;
    font-size: 14px; letter-spacing: 0.6px;
  }
  /* Front side */
  .card-front {
    left: 620px; top: 380px;
    background: var(--white);
    color: var(--navy);
  }
  .card-front .wordmark {
    position: absolute; left: 34px; top: 62px;
    font-size: 27px; color: var(--navy);
  }
  .card-front .wordmark-square { width: 17px; height: 17px; }
  .accreditation-badge {
    position: absolute; right: 30px; top: 28px;
    width: 150px; height: 56px;
    border: 2px solid var(--badge-blue);
    border-radius: 8px;
    background: linear-gradient(90deg, var(--white) 34%, var(--badge-blue) 34%);
  }
  .owner { position: absolute; right: 30px; top: 104px; text-align: right; }
  .owner-name { font-weight: 800; font-size: 24px; color: var(--navy); line-height: 1.1; }
  .owner-title { font-size: 12.5px; color: var(--ink); margin-top: 2px; }
  .divider {
    position: absolute; left: 34px; right: 30px; top: 168px;
    height: 1px; background: var(--navy);
  }
  .contact-list {
    position: absolute; left: 34px; top: 184px;
    list-style: none; font-size: 14px; color: var(--ink);
  }
  .contact-list li { display: flex; align-items: center; gap: 10px; height: 24px; }
  .contact-list svg { width: 13px; height: 13px; fill: var(--navy); flex: none; }
  .address {
    position: absolute; right: 30px; top: 190px;
    text-align: right; font-size: 13px; color: var(--ink); line-height: 1.6;
  }
</style>
</head>
<body>

  <section class="card card-back">
    <div class="wordmark"><span class="wordmark-square"></span>Crestline Roofing</div>
    <p class="license">Contractor License number KMT48395</p>
  </section>

  <section class="card card-front">
    <div class="wordmark"><span class="wordmark-square"></span>Crestline Roofing</div>
    <div class="accreditation-badge" role="img" aria-label="QPL accredited business badge"></div>

    <div class="owner">
      <p class="owner-name">Nora Castell</p>
      <p class="owner-title">Chief Executive Officer</p>
    </div>

    <div class="divider"></div>

    <ul class="contact-list">
      <li>
        <svg viewBox="0 0 16 16" aria-hidden="true"><path d="M3 1l3 3-1.5 2a9 9 0 0 0 5.5 5.5L12 10l3 3-2 2C7 15 1 9 1 3z"/></svg>
        555.214.3087
      </li>
      <li>
        <svg viewBox="0 0 16 16" aria-hidden="true"><rect x="4" y="1" width="8" height="14" rx="1.5"/><rect x="5.5" y="3" width="5" height="8" fill="#fff"/></svg>
        555.468.1902
      </li>
      <li>
        <svg viewBox="0 0 16 16" aria-hidden="true"><path d="M1 3h14v10H1z"/><path d="M1 3l7 6 7-6" fill="none" stroke="#fff" stroke-width="1.4"/></svg>
        nora@crestlineroof.com
      </li>
      <li>
        <svg viewBox="0 0 16 16" aria-hidden="true"><circle cx="8" cy="8" r="7"/><path d="M1 8h14M8 1c3 3 3 11 0 14M8 1c-3 3-3 11 0 14" fill="none" stroke="#fff" stroke-width="1"/></svg>
        www.crestlineroof.com
      </li>
    </ul>

    <p class="address">48 Harlow Lane<br>Fairview MA 01234</p>
  </section>

</body>
</html>
```